Skiing Company Needs A5 28page Skiing Catalogue

ABOUT THE BUSINESS/COMPANY:
- We are a guided skiing company called "Copper Lantern Treks" and "Ridgeway Powder Society".

ABOUT THE CATALOGUE:

- We need an A5 28 page catalogue. ALL THE FILES (like photos and logos) are in the zip folders.

- You can look at the 000 RPS Catalog Word Document. Instructions on what text and photos to use are labeled there per Page.

Target Market(s)

Advanced/ Expert Skiers and Snowboarders that are thinking of joining a tour

Industry/Entity Type

Travel Agent

Font styles to use
Serif

Colors
ffffff
ec1f27
0455a3

Requirements
Must have
• NEED a 3mm bleed
• This is included on the 000 RPS Catalog word document
Nice to have
• Our main color is dark blue (just like our logo). Some red is ok but the main focus should be the dark blue.
Should not have
• Words/ Letters in the color red

```html
<!DOCTYPE html>
<html lang="en">
<head>
<meta charset="utf-8">
<title>2017-18 Product Catalog – Spreads</title>
<link href="https://fonts.googleapis.com/css2?family=Alfa+Slab+One&family=Lato:wght@400;700;900&display=swap" rel="stylesheet">
<style>
  :root{
    --blue:#0455a3;
    --red:#ec1f27;
    --white:#ffffff;
    --ink:#2b2b2b;
    --paper:#f4f4f4;
    --canvas:#e3e4e6;
    --snow-hi:#eef3f8;
    --snow-lo:#9fb6cf;
    --sky:#3b78c2;
  }
  *{box-sizing:border-box;margin:0;padding:0}
  html,body{width:1200px;height:1200px;overflow:hidden;background:var(--canvas)}
  .board{position:relative;width:1200px;height:1200px}
  .page{position:absolute;width:346px;height:484px;background:var(--white);overflow:hidden;
        box-shadow:0 3px 8px rgba(0,0,0,.25);font-family:"Lato",sans-serif;color:var(--ink)}
  .p1{left:28px;top:74px}.p2{left:426px;top:74px}.p3{left:826px;top:74px}
  .p4{left:28px;top:640px}.p5{left:426px;top:640px}.p6{left:826px;top:640px}
  .art{position:absolute;inset:0;width:100%;height:100%}
  .page-title{position:absolute;left:20px;font-family:"Alfa Slab One",serif;font-weight:400;
        color:var(--blue);font-size:19px;letter-spacing:.5px;line-height:1}
  .page-title::before{content:"";position:absolute;left:-20px;top:2px;width:8px;height:14px;background:var(--red)}
  .copy{position:absolute;left:20px;right:20px;font-size:6.1px;line-height:1.32}
  .copy p{margin-bottom:4px}
  .copy b{font-weight:900}
  .copy .hl{color:var(--red);font-weight:700}
  .copy .note{color:var(--blue);font-weight:700}
  /* cover */
  .cover-brand{position:absolute;top:26px;right:22px;display:flex;align-items:center;gap:6px;
        font-size:9px;font-weight:900;color:var(--white)}
  .cover-brand i{width:12px;height:12px;border-radius:50%;background:var(--white);display:block}
  .cover-title{position:absolute;right:20px;top:360px;text-align:right;font-family:"Alfa Slab One",serif;line-height:1.05}
  .cover-title .year{color:var(--blue);font-size:30px}
  .cover-title .product{color:var(--red);font-size:30px}
  .cover-title .catalog{color:#3a3a3a;font-size:22px}
  /* tribute */
  .tribute{position:absolute;left:19px;top:371px;font-size:9.5px;line-height:1.1}
  .tribute strong{display:block;font-family:"Alfa Slab One",serif;font-weight:400;color:var(--red);font-size:14px}
  /* contents */
  .p6{background:linear-gradient(160deg,#ffffff 0%,#eeeff1 60%,#e2e4e7 100%)}
  .p6 .page-title{left:62px}
  .p6 .page-title::before{left:-62px}
  .p6 .corner{position:absolute;right:0;top:17px;width:12px;height:14px;background:var(--red)}
  .toc{position:absolute;left:22px;right:30px;top:58px;list-style:none}
  .toc li{display:flex;align-items:baseline;height:20.4px;font-size:8px;font-weight:700;color:#222}
  .toc li::before{content:"";width:4px;height:6px;background:var(--red);margin-right:37px;flex:none}
  .toc li:nth-child(even)::before{background:var(--blue)}
  .toc .lead{flex:1;border-bottom:1px dotted #555;margin:0 18px 0 3px;transform:translateY(-2px)}
  .toc .pg{width:30px;font-weight:700}
</style>
</head>
<body>
<main class="board">

  <!-- Cover -->
  <section class="page p1">
    <svg class="art" viewBox="0 0 346 484" preserveAspectRatio="none">
      <defs>
        <linearGradient id="coverPhoto" x1="0" y1="0" x2="1" y2="1">
          <stop offset="0" stop-color="#dfe8f2"/><stop offset=".5" stop-color="#a7bdd6"/><stop offset="1" stop-color="#e9eff6"/>
        </linearGradient>
      </defs>
      <rect width="346" height="484" fill="url(#coverPhoto)" role="img" aria-label="Photo: snowboarder descending a steep powder slope beneath a volcano"/>
      <polygon points="0,372 346,292 346,484 0,484" fill="var(--blue)"/>
      <polygon points="0,372 346,292 346,304 0,384" fill="var(--red)"/>
      <polygon points="90,382 346,318 346,484 196,484" fill="var(--red)"/>
      <polygon points="104,386 346,328 346,484 212,484" fill="var(--white)"/>
    </svg>
    <div class="cover-brand"><i></i>Copper Lantern Treks</div>
    <h1 class="cover-title">
      <div class="year">2017-18</div>
      <div class="product">PRODUCT</div>
      <div class="catalog">CATALOG</div>
    </h1>
  </section>

  <!-- About us 1 -->
  <section class="page p2">
    <svg class="art" viewBox="0 0 346 484" preserveAspectRatio="none">
      <defs>
        <linearGradient id="heliPhoto" x1="0" y1="0" x2="0" y2="1">
          <stop offset="0" stop-color="var(--sky)"/><stop offset=".55" stop-color="#8fb3dc"/><stop offset="1" stop-color="#e8eef5"/>
        </linearGradient>
      </defs>
      <polygon points="0,140 346,132 346,484 0,484" fill="url(#heliPhoto)" role="img" aria-label="Photo: skiers loading gear into a helicopter on a snowy summit"/>
      <polygon points="0,134 220,130 346,150 346,140 220,126 0,130" fill="var(--red)"/>
      <polygon points="0,140 200,134 200,136 0,142" fill="var(--blue)"/>
    </svg>
    <h2 class="page-title" style="top:20px">ABOUT US</h2>
    <div class="copy" style="top:56px">
      <p>Welcome to our 14th season of Cedar Hearth Lodge, Copper Lantern Treks and Summit Road Auto. The 2018 season also marks our 5th season of the Ridgeway Powder Society, our mechanized wing of TRV Trading.</p>
      <p>TRV (which stands for Trail Road Voyage) was established in Oct of 2003 when our founder Miles Hartwell went "all in" and decided to purchase a lodge in Higashiyama to serve as a base to finally pursue his dream of starting a tour company dedicated to hardcore skiers and boarders while also offering a low cost rental car alternative allowing expat families and friends the ability to explore the wonders of Hokkaido on their own.</p>
    </div>
  </section>

  <!-- About us 2 -->
  <section class="page p3">
    <svg class="art" viewBox="0 0 346 484" preserveAspectRatio="none">
      <defs>
        <linearGradient id="lodgePhoto" x1="0" y1="0" x2="0" y2="1">
          <stop offset="0" stop-color="#c9d7e6"/><stop offset=".45" stop-color="#6a4a3a"/><stop offset="1" stop-color="#f3f5f8"/>
        </linearGradient>
        <linearGradient id="sledPhoto" x1="0" y1="0" x2="1" y2="1">
          <stop offset="0" stop-color="#b8cbe0"/><stop offset=".6" stop-color="#dde6f0"/><stop offset="1" stop-color="#f5f7fa"/>
        </linearGradient>
      </defs>
      <rect width="346" height="190" fill="url(#lodgePhoto)" role="img" aria-label="Photo: wooden lodge building buried in deep snow"/>
      <path d="M0,150 C90,130 200,190 346,160 L346,200 L0,200 Z" fill="var(--white)"/>
      <polygon points="0,320 346,306 346,484 0,484" fill="url(#sledPhoto)" role="img" aria-label="Photo: rider on a snowmobile spraying snow above forested valleys"/>
      <polygon points="0,316 346,300 346,306 0,322" fill="var(--blue)"/>
    </svg>
    <h2 class="page-title" style="top:166px">ABOUT US</h2>
    <div class="copy" style="top:200px">
      <p>A lot has transpired in the past 14 years. Tours grew from just a single guide to a world class team of over 16 guides with experience and training from around the world, our vehicle rental program has grown to include everything from budget to baller, our lodge has seen a plethora of upgrades and RPS was born and now offers Japan's best snowmobile, heli and cat tours.</p>
      <p>While change is inevitable, two things remain constant for us:<br>
      <b>① Our love of sharing Hokkaido's incredible natural assets with you, our valued guests<br>
      ② Our passion to help make Hokkaido a world class adventure sports destination.</b></p>
      <p>Becoming world class can only be accomplished by hard work, determination, education and cooperation. The road has been very difficult at times but as we all know, few things in life worth doing come easy. With your continued support and feedback, Hokkaido WILL get there!</p>
    </div>
  </section>

  <!-- Evolution -->
  <section class="page p4">
    <svg class="art" viewBox="0 0 346 484" preserveAspectRatio="none">
      <defs>
        <linearGradient id="valleyPhoto" x1="0" y1="0" x2="0" y2="1">
          <stop offset="0" stop-color="#5c8fcf"/><stop offset=".35" stop-color="#dfe7f1"/><stop offset="1" stop-color="#7d8a99"/>
        </linearGradient>
      </defs>
      <polygon points="0,216 175,196 346,212 346,484 0,484" fill="url(#valleyPhoto)" role="img" aria-label="Aerial photo: snow-covered volcano above a wintry valley town"/>
      <polygon points="0,206 175,194 346,208 346,214 175,198 0,214" fill="var(--blue)"/>
      <polygon points="175,194 346,202 346,208 175,198" fill="var(--red)"/>
    </svg>
    <h2 class="page-title" style="top:20px">EVOLUTION OF NISEKO</h2>
    <div class="copy" style="top:58px">
      <p>With increased numbers of foreign travelers, resorts around Hokkaido have also undergone many changes. Along with new lifts and developments, many resorts have now instituted a long overdue open gate/backcountry policy to help satisfy the undeniable and rapidly increasing backcountry skier/boarder market. Each resort has a slightly different twist, so please be sure to check in with us or the resort to find out the latest. While Niseko Peaks Group has recently invested heavily into the growing beginner Asian market with 4 new lifts, little has been dedicated to the hardcore powder junkies. Please be sure to let the local tourism board that you (like us) want the more and ask them when they will finally <u>open and control</u> <b>Yunosawa</b> and <b>Harunotaki</b>.</p>
      <p>Despite our consistent weather and relatively stable snowpack, with all this wind and snowfall, accidents DO happen in Hokkaido. Since 1937, there has been 103 individuals that have reported an encounter with an avalanche in Niseko, and unfortunately 15 people have lost their lives. Given the negative press and connotation of a backcountry "accident" we suspect there have been MANY more that have gone unreported. Please be careful out there and be prepared for self rescue no matter where you are.</p>
    </div>
  </section>

  <!-- Fatalities -->
  <section class="page p5">
    <svg class="art" viewBox="0 0 346 484" preserveAspectRatio="none">
      <defs>
        <radialGradient id="portraitPhoto" cx=".55" cy=".6" r=".6">
          <stop offset="0" stop-color="#c9c2b8"/><stop offset=".6" stop-color="#d9d4c4"/><stop offset="1" stop-color="#ffffff"/>
        </radialGradient>
      </defs>
      <rect x="90" y="186" width="256" height="298" fill="url(#portraitPhoto)" role="img" aria-label="Photo: snow-covered rider in goggles and yellow jacket, in memoriam"/>
    </svg>
    <h2 class="page-title" style="top:20px">FATALITIES IN NISEKO</h2>
    <div class="copy" style="top:58px">
      <p>On February 25th Niseko lost a legend. <span class="hl">Dan Ashby</span>, loving husband, father, mountain and rafting guide lost his life to an avalanche on the southeast face of <b>Haru-no-taki</b>. The snow was incredible that day, but the crowds and lift lines were even more so. When you use a lift and/or you're in competition for fresh powder, decisions get made much faster as was the case on that very day. People enter these areas because they offer the steepest and best fall-line riding in the area and they are so easily accessed. Simply out, people duck these ropes because these areas never open. If these areas were controlled and managed, we believe that people would wait and locals would self police and strongly enforce these policies. If you give advanced skiers and boarders the opportunity to actually ski these areas, they will respect you back and follow the rules. 4 years ago we lost a wonderful neighbor and father of three when he skied into a fresh glide crack in the Yunosawa area. Had this area been managed, he may still be with us today. Let's not let these losses go in vain. Together we can make positive change happen.</p>
      <p><span class="note">Note:</span> CHL and T are trying to make a positive change and this is why we asking all of guests to follow the current rules.</p>
    </div>
    <div class="tribute">We miss you<strong>DASHDOG</strong></div>
  </section>

  <!-- Contents -->
  <section class="page p6">
    <svg class="art" viewBox="0 0 346 484" preserveAspectRatio="none">
      <polygon points="0,452 346,452 346,484 0,484" fill="var(--blue)"/>
      <polygon points="120,484 346,452 346,484" fill="var(--red)"/>
      <polygon points="0,452 346,452 346,450 0,450" fill="var(--white)" opacity="0"/>
      <polygon points="0,444 346,452 0,452" fill="#e6e8eb"/>
    </svg>
    <h2 class="page-title" style="top:20px">TABLE OF CONTENTS</h2>
    <span class="corner"></span>
    <ol class="toc">
      <li>2017-18 Product Catalog<span class="lead"></span><span class="pg">1</span></li>
      <li>About Us<span class="lead"></span><span class="pg">2 - 3</span></li>
      <li>Evolution of Niseko<span class="lead"></span><span class="pg">4</span></li>
      <li>Fatalities in Niseko<span class="lead"></span><span class="pg">5</span></li>
      <li>Table of Contents<span class="lead"></span><span class="pg">6</span></li>
      <li>Guides<span class="lead"></span><span class="pg">7</span></li>
      <li>Multi-day Trip Comparison Chart<span class="lead"></span><span class="pg">8</span></li>
      <li>Day Trip Comparison Chart<span class="lead"></span><span class="pg">9</span></li>
      <li>Shimamaki Snowcats<span class="lead"></span><span class="pg">10 - 11</span></li>
      <li>information about our tours<span class="lead"></span><span class="pg">12 - 13</span></li>
      <li>Motta Onsen<span class="lead"></span><span class="pg">14</span></li>
      <li>Chihasegawa Onsen<span class="lead"></span><span class="pg">15</span></li>
      <li>Backcountry Touring Day Trips<span class="lead"></span><span class="pg">16</span></li>
      <li>Lift Assisted Backcountry Day Trips<span class="lead"></span><span class="pg">17</span></li>
      <li>Yotei Summit Tours<span class="lead"></span><span class="pg">18 - 19</span></li>
      <li>Multi-day Tours<span class="lead"></span><span class="pg">20 - 23</span></li>
      <li>Avalanche Courses<span class="lead"></span><span class="pg">24 - 25</span></li>
      <li>Partners<span class="lead"></span><span class="pg">26</span></li>
      <li>Contact Us<span class="lead"></span><span class="pg">27</span></li>
    </ol>
  </section>

</main>
</body>
</html>
```